December online webinar for our coaching and mentoring business.

needing an email flyer and something to use on appropriate social media e.g. Instagram to promote our December half day webinar focusing on positive mindset, relationships and 2021 being a new year with new opportunities. For the feel of what we have done previously:
www.qlvgetaways.com.au
We will be using 2 guest speakers:
Marcus Elwood of BucketGoals.com and
Lorena Voss, psychologist and both will need to be prominent on the marketing material we send out on email and use on social media.
The webinar will likely run Thursday December 10th from 12.30pm to 4.30pm AEST and will be hosted and facilitated by me and on behalf of Tarrow Business Coaching.
I am thinking colour schemes and branding similar to what you see on the website above.
Pricing needs to be on the flyer - $750 + GST per person*
*enquire for multi booking discounts for 2 people or more

Target Market(s)

people looking for a boost before the year end and a fast start to 2021

Font styles to use
Sans Serif

Requirements
Must have
• see brief above
Nice to have
• see brief above
Should not have
• see brief above

```html
<!DOCTYPE html>
<html lang="en">
<head>
<meta charset="utf-8">
<title>Positive Mindset Relationships 2021 – Webinar</title>
<link rel="stylesheet" href="https://fonts.googleapis.com/css2?family=Inter:wght@300;400;500;700;800;900&family=Open+Sans:wght@400;600;700&display=swap">
<style>
  :root {
    --page-bg: #fbe6e7;
    --red: #ee3e36;
    --red-dark: #c9302b;
    --red-deep: #a8201c;
    --black: #0f0f0f;
    --black-soft: #1c1c1c;
    --white: #ffffff;
    --grey-text: #6f6f6f;
    --grey-light: #f7f7f7;
    --footer-text: #7a7a7a;
  }
  * { box-sizing: border-box; margin: 0; padding: 0; }
  html, body { width: 1161px; height: 1200px; overflow: hidden; background: var(--page-bg); }
  .stage {
    position: absolute; left: 0; top: 0;
    width: 1204px; height: 1244px;
    transform: scale(0.9643); transform-origin: 0 0;
    font-family: "Inter", sans-serif;
  }
  .flyer {
    position: absolute; left: 305px; top: 57px;
    width: 600px; height: 1079px;
    background: var(--black); overflow: hidden;
    box-shadow: 0 20px 50px rgba(120, 40, 40, 0.12);
  }
  .abs { position: absolute; }
  .backdrop { position: absolute; left: 0; top: 0; width: 600px; height: 1006px; }

  .brand-mark {
    left: 15px; top: 17px;
    color: var(--white); font-weight: 800; font-size: 21px; letter-spacing: -0.5px;
  }
  .header-tagline {
    left: 150px; width: 380px; top: 25px; text-align: center;
    color: var(--white); font-size: 14.5px; font-weight: 400;
  }

  .date-line {
    left: 0; width: 600px; top: 121px; text-align: center;
    color: var(--white); font-family: "Open Sans", sans-serif; font-size: 18px;
  }
  .date-tag {
    display: inline-block; position: relative; margin-left: 3px;
    padding: 0 12px 0 6px; color: var(--red); font-weight: 700; font-size: 17px;
    background: var(--white);
    clip-path: polygon(0 0, 100% 0, 92% 100%, 0 100%);
    line-height: 22px;
  }
  .event-title {
    left: 0; width: 600px; top: 163px; text-align: center;
    color: var(--white); font-weight: 800; font-size: 52px;
    line-height: 48px; letter-spacing: -1.8px;
  }
  .event-year {
    left: 0; width: 600px; top: 278px; text-align: center;
    color: var(--white); font-weight: 900; font-size: 74px; letter-spacing: -2px;
  }
  .from-label {
    left: 0; width: 600px; top: 379px; text-align: center;
    color: var(--white); font-size: 14px; font-weight: 500; letter-spacing: 2px;
  }
  .time-band {
    left: 160px; width: 284px; top: 409px; height: 31px;
    background: var(--red-deep);
    clip-path: polygon(2% 0, 100% 0, 98% 100%, 0 100%);
    color: var(--white); font-family: "Open Sans", sans-serif; font-size: 21px;
    text-align: center; line-height: 31px;
  }
  .register-shadow {
    left: 222px; top: 464px; width: 161px; height: 52px;
    border: 1px solid var(--black);
  }
  .register-button {
    left: 216px; top: 458px; width: 161px; height: 51px;
    background: var(--black); color: var(--white);
    font-family: "Open Sans", sans-serif; font-weight: 700; font-size: 15.5px;
    text-align: center; line-height: 51px;
  }

  .speaker-ring {
    width: 156px; height: 156px; border-radius: 50%;
    border: 1.5px solid var(--white); padding: 4px;
  }
  .speaker-photo {
    width: 100%; height: 100%; border-radius: 50%;
    background: linear-gradient(160deg, #f3e7e4 0%, #e9d6cf 55%, #3a7d6e 100%);
  }
  .speaker-photo.is-marcus { background: linear-gradient(160deg, #f1e6e3 0%, #d7b69f 55%, #4a4a4a 100%); }
  .speaker-left { left: 41px; top: 482px; }
  .speaker-right { left: 402px; top: 482px; }
  .name-tag {
    top: 621px; height: 25px; background: var(--white);
    clip-path: polygon(6% 0, 100% 0, 94% 100%, 0 100%);
    color: var(--black); font-weight: 800; font-style: italic; font-size: 12px;
    text-align: center; line-height: 25px; text-transform: uppercase;
  }
  .name-left { left: 49px; width: 142px; }
  .name-right { left: 410px; width: 143px; }
  .speaker-role {
    color: var(--white); font-family: "Open Sans", sans-serif; font-size: 13px; text-align: center;
  }
  .role-left { left: 49px; width: 142px; top: 660px; }
  .role-right { left: 400px; width: 165px; top: 656px; }

  .price {
    left: 0; width: 600px; top: 642px; text-align: center;
    color: var(--white); font-family: "Open Sans", sans-serif; font-weight: 700; font-size: 28px;
  }
  .price-unit {
    left: 0; width: 600px; top: 681px; text-align: center;
    color: var(--white); font-family: "Open Sans", sans-serif; font-size: 18px;
  }
  .price-note {
    left: 0; width: 600px; top: 721px; text-align: center;
    color: var(--grey-text); font-size: 14.5px; line-height: 18px; letter-spacing: 0.4px;
  }
  .divider {
    left: 55px; width: 490px; top: 796px; border-top: 1px dashed #4a4a4a;
  }
  .host-label {
    left: 0; width: 600px; top: 822px; text-align: center;
    color: var(--white); font-size: 13px; font-weight: 500; letter-spacing: 2px;
  }
  .host-name {
    left: 0; width: 600px; top: 845px; text-align: center;
    color: #565656; font-weight: 300; font-size: 22px; letter-spacing: 0.4px;
  }
  .host-mark {
    left: 0; width: 600px; top: 910px; text-align: center;
    color: var(--white); font-weight: 800; font-size: 34px; letter-spacing: -0.5px;
  }
  .contact-bar {
    left: 0; top: 1006px; width: 600px; height: 73px;
    background: var(--grey-light); color: var(--footer-text);
    font-size: 14px; text-align: center; line-height: 73px;
  }
  .contact-bar .sep { margin: 0 8px; }
</style>
</head>
<body>
<div class="stage">
  <article class="flyer">
    <svg class="backdrop" viewBox="0 0 600 1006" aria-hidden="true">
      <rect x="0" y="80" width="600" height="480" fill="var(--red)"/>
      <polygon points="0,205 600,330 600,400 0,270" fill="var(--red-dark)" opacity="0.55"/>
      <polygon points="410,80 465,80 555,170 555,230" fill="#ffffff" opacity="0.12"/>
      <polygon points="555,170 600,125 600,190 555,230" fill="#ffffff" opacity="0.12"/>
      <polygon points="0,285 130,415 90,455 0,360" fill="#ffffff" opacity="0.08"/>
      <polygon points="355,560 485,418 530,460 440,560" fill="#ffffff" opacity="0.1"/>
      <polygon points="485,418 600,530 600,560 560,560 470,470" fill="#ffffff" opacity="0.08"/>
      <rect x="0" y="0" width="600" height="80" fill="var(--black-soft)"/>
      <polygon points="560,80 600,0 600,80" fill="#0a0a0a"/>
      <polygon points="0,0 170,0 0,140" fill="var(--red)"/>
      <polygon points="170,0 150,0 0,125 0,140" fill="var(--red-deep)"/>
      <polygon points="268,560 332,560 300,592" fill="var(--red)"/>
      <polygon points="288,553 312,553 300,564" fill="var(--white)"/>
    </svg>

    <div class="abs brand-mark">Tarrow</div>
    <p class="abs header-tagline">webinar for our coaching and mentoring business</p>

    <p class="abs date-line">Thursday <span class="date-tag">December 10th</span></p>
    <h1 class="abs event-title">positive mindset<br>relationships</h1>
    <p class="abs event-year">2021</p>
    <p class="abs from-label">FROM</p>
    <p class="abs time-band">12.30pm to 4.30pm AEST</p>
    <div class="abs register-shadow"></div>
    <div class="abs register-button">Register Now</div>

    <div class="abs speaker-ring speaker-left">
      <div class="speaker-photo" role="img" aria-label="Portrait photo of speaker Lorena Voss"></div>
    </div>
    <div class="abs speaker-ring speaker-right">
      <div class="speaker-photo is-marcus" role="img" aria-label="Portrait photo of speaker Marcus Elwood"></div>
    </div>
    <div class="abs name-tag name-left">Lorena Voss</div>
    <div class="abs name-tag name-right">Marcus Elwood</div>
    <p class="abs speaker-role role-left">psychologist</p>
    <p class="abs speaker-role role-right">of BucketGoals.com</p>

    <p class="abs price">$750 + GST</p>
    <p class="abs price-unit">Per person</p>
    <p class="abs price-note">enquire for multi booking<br>discounts for 2 people or more</p>

    <div class="abs divider"></div>
    <p class="abs host-label">HOST</p>
    <p class="abs host-name">Tarrow Business Coaching</p>
    <div class="abs host-mark">Tarrow</div>

    <footer class="abs contact-bar">
      0400 517 382<span class="sep">I</span>james@tarrowcoaching.com.au<span class="sep">I</span>Connect
    </footer>
  </article>
</div>
</body>
</html>
```